Illustration of business process for corporate demonstration

Update 27-05-13
Primary - Illustrate the below the line process with "iconology" for each step e.g:
Icon for visio
Icno for develop brief
Icon for market research
And so on for each step for a total of 21

The top line logo for Innovate and Implement large icons to be refined but intent to remain the same. The final icon/Meridian Oakfold logo is NOT to be changed.

Meridian Oakfold is a consultancy that specialises in assisting businesses to realise their innovation aspirations via a proven Growth Trailmap – for more information please see the draft web page at https://tobias-renwald.examplesite.net/

I require a visual representation of the attached process that is easy to understand and also visually stunning. You will notice that the icons above Innovate, Implement Thrive build to form the Meridian Oakfold logo. This concept of building to form individual elements to complete an outcome is core to the Meridian Oakfold method and needs to clearly visible for a submission to be successful.

Target Market(s)

Company owners, directors and senior executives that are looking to more innovate in their business but are time and/or resources poor.

Industry/Entity Type

Building

Requirements
Must have
• The Meridian Oakfold final logo must not be changed in any way.

The images above Innovate and Thrive should be stylised to suit as they are only mock-ups to illustrate the concept.

Must be 1 page to suit online publication and in print materials
Should not have
• Do not change/amend the logo!

```html
<!DOCTYPE html>
<html lang="en">
<head>
<meta charset="utf-8">
<title>Meridian Oakfold – Growth Trailmap</title>
<link rel="stylesheet" href="https://fonts.googleapis.com/css2?family=Ubuntu:wght@400;500;700&family=Open+Sans:wght@400;600;700&family=Exo:wght@700;800&display=swap">
<style>
  :root {
    --green: #6aa321;
    --green-dark: #4e7d1b;
    --green-deep: #2f5a12;
    --ink: #3e3e3e;
    --text: #555555;
    --grey-icon: #666666;
    --header-top: #d9dadb;
    --header-bottom: #f3f3f3;
    --page-top: #ffffff;
    --page-bottom: #efefec;
    --arrow-light: #e6cf9e;
    --arrow-dark: #9c7a3c;
    --earth: #3f5d6e;
    --skin: #e9b8a4;
  }
  * { margin: 0; padding: 0; box-sizing: border-box; }
  html, body { width: 1200px; height: 900px; overflow: hidden; }
  body {
    background: linear-gradient(180deg, var(--page-top) 30%, var(--page-bottom) 100%);
    font-family: "Open Sans", Arial, sans-serif;
    color: var(--text);
  }
  .canvas { position: relative; width: 1200px; height: 900px; }

  .masthead {
    position: absolute; inset: 0 0 auto 0; height: 178px;
    background: linear-gradient(180deg, var(--header-top), var(--header-bottom));
    border-bottom: 1px solid #e2e2e2;
  }
  .brand { position: absolute; left: 420px; top: 24px; display: flex; align-items: center; gap: 22px; }
  .brand-dot { width: 74px; height: 74px; border-radius: 50%; background: var(--green); }
  .brand-name {
    font-family: "Ubuntu", sans-serif; font-weight: 700; font-size: 46px; line-height: 44px;
    color: var(--green); text-transform: uppercase; letter-spacing: 1px;
  }
  .brand-tagline {
    margin-top: 8px; font-family: "Ubuntu", sans-serif; font-weight: 500; font-size: 17px;
    letter-spacing: 2px; color: var(--ink); text-transform: uppercase;
  }

  .page-title {
    position: absolute; top: 196px; left: 0; width: 100%; text-align: center;
    font-family: "Exo", sans-serif; font-weight: 800; font-size: 36px; letter-spacing: 2px;
    color: var(--green); text-transform: uppercase;
  }

  .stage-art { position: absolute; }
  .art-mind { left: 228px; top: 292px; width: 135px; height: 188px;
    background: radial-gradient(circle at 55% 35%, #9fd15a 0%, var(--green) 35%, var(--green-deep) 100%);
    border-radius: 60% 45% 30% 30%; }
  .art-hand { left: 508px; top: 338px; width: 176px; height: 128px;
    background: linear-gradient(180deg, var(--green) 0%, var(--green) 35%, var(--skin) 60%, #d89d86 100%);
    border-radius: 40% 40% 30% 30%; }
  .art-earth { left: 812px; top: 292px; width: 196px; height: 190px;
    background: linear-gradient(180deg, var(--green) 0%, var(--green-dark) 45%, #8a6a3a 60%, var(--earth) 80%, #2b4454 100%);
    border-radius: 50% 50% 8px 8px; }

  .stage-name {
    position: absolute; top: 494px; font-family: "Ubuntu", sans-serif; font-weight: 700;
    font-size: 36px; color: var(--green); width: 260px; text-align: center;
  }
  .name-innovate { left: 148px; }
  .name-implement { left: 476px; }
  .name-thrive { left: 784px; }

  .flow-arrow { position: absolute; top: 503px; width: 70px; height: 36px; }
  .arrow-one { left: 404px; }
  .arrow-two { left: 753px; }

  .step-list { position: absolute; top: 576px; list-style: none; }
  .step-list li { height: 36px; font-size: 16.5px; line-height: 28px; position: relative; white-space: nowrap; }
  .step-list .list-head { font-weight: 700; color: var(--green-dark); }
  .list-innovate { left: 140px; }
  .list-implement { left: 525px; }
  .list-thrive { left: 879px; }
  .step-icon { position: absolute; left: -52px; top: 0; width: 30px; height: 28px; }
</style>
</head>
<body>
<main class="canvas">
  <header class="masthead">
    <div class="brand">
      <span class="brand-dot"></span>
      <div>
        <div class="brand-name">Meridian<br>Oakfold</div>
        <div class="brand-tagline">Innovate - Implement - Thrive</div>
      </div>
    </div>
  </header>

  <h1 class="page-title">Growth Trailmap</h1>

  <div class="stage-art art-mind" role="img" aria-label="Green patterned head silhouette with a lightbulb and sprouting seedling inside"></div>
  <div class="stage-art art-hand" role="img" aria-label="Open hand holding soil with a young green seedling"></div>
  <div class="stage-art art-earth" role="img" aria-label="Large green tree growing on top of the globe"></div>

  <h2 class="stage-name name-innovate">Innovate</h2>
  <h2 class="stage-name name-implement">Implement</h2>
  <h2 class="stage-name name-thrive">Thrive</h2>

  <svg class="flow-arrow arrow-one" viewBox="0 0 70 36" aria-hidden="true">
    <defs><linearGradient id="arrowFill" x1="0" x2="1"><stop offset="0" stop-color="#e6cf9e"/><stop offset="1" stop-color="#9c7a3c"/></linearGradient></defs>
    <polygon points="0,9 40,9 40,0 70,18 40,36 40,27 0,27" fill="url(#arrowFill)"/>
  </svg>
  <svg class="flow-arrow arrow-two" viewBox="0 0 70 36" aria-hidden="true">
    <polygon points="0,9 40,9 40,0 70,18 40,36 40,27 0,27" fill="url(#arrowFill)"/>
  </svg>

  <ul class="step-list list-innovate">
    <li class="list-head">Refine concept:</li>
    <li><svg class="step-icon" viewBox="0 0 30 28" aria-hidden="true"><path d="M2 14 Q15 3 28 14 Q15 25 2 14Z" fill="none" stroke="#555" stroke-width="2"/><circle cx="15" cy="14" r="5" fill="var(--green)"/></svg>Vision – your goal</li>
    <li><svg class="step-icon" viewBox="0 0 30 28" aria-hidden="true"><path d="M8 2 H19 L24 7 V26 H8Z" fill="#fff" stroke="var(--green-dark)" stroke-width="2"/><path d="M19 2 V7 H24" fill="none" stroke="var(--green-dark)" stroke-width="2"/></svg>Develop Brief</li>
    <li><svg class="step-icon" viewBox="0 0 30 28" aria-hidden="true"><circle cx="17" cy="10" r="7" fill="none" stroke="var(--green-dark)" stroke-width="3"/><line x1="12" y1="15" x2="4" y2="25" stroke="var(--green-dark)" stroke-width="4" stroke-linecap="round"/></svg>Market Research</li>
    <li><svg class="step-icon" viewBox="0 0 30 28" aria-hidden="true"><ellipse cx="15" cy="21" rx="9" ry="4" fill="#666"/><ellipse cx="15" cy="15" rx="9" ry="4" fill="var(--green)"/><ellipse cx="15" cy="8" rx="9" ry="4" fill="var(--green-dark)"/></svg>Define Value</li>
    <li><svg class="step-icon" viewBox="0 0 30 28" aria-hidden="true"><rect x="7" y="2" width="16" height="24" rx="2" fill="none" stroke="var(--green-dark)" stroke-width="2"/><rect x="10" y="5" width="10" height="5" fill="var(--green)"/><g fill="var(--green-dark)"><rect x="10" y="13" width="3" height="3"/><rect x="14" y="13" width="3" height="3"/><rect x="18" y="13" width="2" height="3"/><rect x="10" y="18" width="3" height="3"/><rect x="14" y="18" width="3" height="3"/><rect x="18" y="18" width="2" height="3"/></g></svg>Budget Project</li>
    <li><svg class="step-icon" viewBox="0 0 30 28" aria-hidden="true"><circle cx="15" cy="14" r="11" fill="none" stroke="var(--green-dark)" stroke-width="2.5"/><path d="M9 14 L13 18 L21 9" fill="none" stroke="var(--green-dark)" stroke-width="3"/></svg>Allocate Resources</li>
    <li><svg class="step-icon" viewBox="0 0 30 28" aria-hidden="true"><circle cx="15" cy="14" r="11" fill="var(--green)"/><path d="M19 9.5 Q15 7 12 9 Q10 11.5 14 13.5 Q19 15 18 18 Q15 21 11 18.5" fill="none" stroke="#fff" stroke-width="2"/><line x1="15" y1="5.5" x2="15" y2="22.5" stroke="#fff" stroke-width="1.6"/></svg>Identify Funding</li>
  </ul>

  <ul class="step-list list-implement">
    <li class="list-head">Drive outcomes:</li>
    <li><svg class="step-icon" viewBox="0 0 30 28" aria-hidden="true"><rect x="6" y="4" width="18" height="22" rx="2" fill="none" stroke="var(--green-dark)" stroke-width="2"/><rect x="11" y="2" width="8" height="4" rx="1" fill="var(--green)"/><path d="M9 12 L11 14 L14 10 M9 19 L11 21 L14 17" fill="none" stroke="var(--green)" stroke-width="1.8"/><path d="M16 12 H21 M16 19 H21" stroke="#666" stroke-width="1.8"/></svg>Project accountability</li>
    <li><svg class="step-icon" viewBox="0 0 30 28" aria-hidden="true"><path d="M3 10 L15 3 L27 10Z" fill="var(--green-dark)"/><g fill="var(--green)"><rect x="6" y="12" width="3" height="9"/><rect x="13.5" y="12" width="3" height="9"/><rect x="21" y="12" width="3" height="9"/></g><rect x="3" y="22" width="24" height="3" fill="#666"/></svg>Source funding</li>
    <li><svg class="step-icon" viewBox="0 0 30 28" aria-hidden="true"><circle cx="15" cy="14" r="8" fill="none" stroke="var(--green-dark)" stroke-width="5" stroke-dasharray="4 2.3"/><circle cx="15" cy="14" r="6" fill="none" stroke="var(--green-dark)" stroke-width="2.5"/><circle cx="15" cy="14" r="2.5" fill="var(--green)"/></svg>Program Development</li>
    <li><svg class="step-icon" viewBox="0 0 30 28" aria-hidden="true"><path d="M6 23 L16 13" stroke="var(--green-dark)" stroke-width="4" stroke-linecap="round"/><path d="M17 6 A6 6 0 1 0 23 12 L20 12 L17 9Z" fill="var(--green)"/></svg>Operation Capabilities</li>
    <li><svg class="step-icon" viewBox="0 0 30 28" aria-hidden="true"><rect x="5" y="15" width="4" height="10" fill="var(--green)"/><rect x="11" y="10" width="4" height="15" fill="var(--green-dark)"/><rect x="17" y="13" width="4" height="12" fill="var(--green)"/><rect x="23" y="5" width="4" height="20" fill="var(--green-dark)"/><line x1="3" y1="26" x2="28" y2="26" stroke="#666" stroke-width="1.5"/></svg>Financial Modelling</li>
    <li><svg class="step-icon" viewBox="0 0 30 28" aria-hidden="true"><path d="M15 3 L27 25 H3Z" fill="none" stroke="var(--green-dark)" stroke-width="2.2" stroke-linejoin="round"/><line x1="15" y1="10" x2="15" y2="18" stroke="var(--green)" stroke-width="2.5"/><circle cx="15" cy="21.5" r="1.5" fill="var(--green)"/></svg>Risk Management</li>
    <li><svg class="step-icon" viewBox="0 0 30 28" aria-hidden="true"><path d="M3 4 H18 V14 H9 L5 18 V14 H3Z" fill="var(--green)"/><path d="M12 11 H27 V21 H25 V25 L21 21 H12Z" fill="none" stroke="var(--green-dark)" stroke-width="2"/></svg>Client Engagement</li>
  </ul>

  <ul class="step-list list-thrive">
    <li class="list-head">Manage Results:</li>
    <li><svg class="step-icon" viewBox="0 0 30 28" aria-hidden="true"><path d="M15 2 L18.5 10 L27 10.5 L20.5 16 L22.5 25 L15 20.5 L7.5 25 L9.5 16 L3 10.5 L11.5 10Z" fill="var(--green)"/></svg>Innovation culture</li>
    <li><svg class="step-icon" viewBox="0 0 30 28" aria-hidden="true"><circle cx="15" cy="14" r="11" fill="none" stroke="var(--green-dark)" stroke-width="2"/><circle cx="15" cy="14" r="6.5" fill="none" stroke="var(--green)" stroke-width="2"/><circle cx="15" cy="14" r="2.5" fill="var(--green-dark)"/></svg>Management Strategy</li>
    <li><svg class="step-icon" viewBox="0 0 30 28" aria-hidden="true"><path d="M3 24 H27 M3 24 V4" stroke="#666" stroke-width="1.5" fill="none"/><path d="M5 21 L11 15 L15 18 L24 8" fill="none" stroke="var(--green-dark)" stroke-width="2.5"/><path d="M19 7 H25 V13" fill="none" stroke="var(--green-dark)" stroke-width="2.5"/></svg>Revenue Forecasting</li>
    <li><svg class="step-icon" viewBox="0 0 30 28" aria-hidden="true"><path d="M4 11 H10 L22 4 V24 L10 17 H4Z" fill="var(--green)"/><path d="M8 17 L10 25 H14 L12 17" fill="var(--green-dark)"/><path d="M25 10 Q28 14 25 18" fill="none" stroke="#666" stroke-width="1.8"/></svg>Promotional Activity</li>
    <li><svg class="step-icon" viewBox="0 0 30 28" aria-hidden="true"><circle cx="15" cy="14" r="11" fill="var(--green)"/><path d="M15 14 V3 A11 11 0 0 1 25.5 17.3Z" fill="var(--green-dark)"/><path d="M15 14 L25.5 17.3 A11 11 0 0 1 19 24.3Z" fill="#666"/></svg>Business Processes &amp; KPI's</li>
    <li><svg class="step-icon" viewBox="0 0 30 28" aria-hidden="true"><rect x="2" y="9" width="15" height="11" fill="var(--green)"/><path d="M17 12 H23 L27 16 V20 H17Z" fill="var(--green-dark)"/><circle cx="8" cy="22" r="3" fill="#666"/><circle cx="22" cy="22" r="3" fill="#666"/></svg>Supply chain engagement</li>
    <li><svg class="step-icon" viewBox="0 0 30 28" aria-hidden="true"><rect x="4" y="5" width="22" height="20" rx="2" fill="none" stroke="var(--green-dark)" stroke-width="2"/><rect x="4" y="5" width="22" height="5" fill="var(--green-dark)"/><line x1="10" y1="2" x2="10" y2="7" stroke="#666" stroke-width="2"/><line x1="20" y1="2" x2="20" y2="7" stroke="#666" stroke-width="2"/><path d="M9 21 L13 17 L16 19 L21 13" fill="none" stroke="var(--green)" stroke-width="2"/></svg>Growth Planning</li>
  </ul>
</main>
</body>
</html>
```